Bill board design For Marlowe’s Construction

Billboard Design Request
Please design the billboard to match the branding, colors, and overall feel of our website: Marlowe's Construction Website
MARLOWE’S CONSTRUCTION
CONCRETE BUILT FOR GENERATIONS
⭐ 5-Star Rated on Zorvix
Please Include:
* All three attached project photos
* Company logo(s)
* Phone Number: 555-214-7630
* Website: MarlowesConstruction.example
* Zorvix logo with 5-star rating graphic
* Chatterly logo
* Pixtoria logo
Service Area:
Kalamazoo • Battle Creek • Coldwater • Grand Rapids
Please arrange the photos and layout in whatever way creates the strongest visual impact and readability from the road. The company name, headline, phone number, and website should be highly visible at highway speeds.
The overall appearance should be clean, professional, premium, and consistent with our website branding while highlighting our reputation, craftsmanship, and quality concrete work.
People Driving By
Concrete Construction

```html
<!DOCTYPE html>
<html lang="en">
<head>
<meta charset="utf-8">
<title>Marlowe's Construction Billboard</title>
<link href="https://fonts.googleapis.com/css2?family=Poppins:wght@400;500;600;700;800&display=swap" rel="stylesheet">
<style>
  :root {
    --page: #e2e2e2;
    --ink: #000000;
    --brand-blue: #1a8fe3;
    --white: #ffffff;
    --muted: #9aa3ab;
  }
  * { box-sizing: border-box; margin: 0; padding: 0; }
  html, body { width: 1043px; height: 1200px; overflow: hidden; }
  body {
    background: var(--page);
    font-family: "Poppins", sans-serif;
    position: relative;
  }
  .billboard {
    position: absolute;
    left: 31px; top: 457px;
    width: 980px; height: 286px;
    background: var(--ink);
    box-shadow: 0 14px 30px rgba(0,0,0,.28);
    overflow: hidden;
  }
  .brand {
    position: absolute; left: 27px; top: 94px; width: 140px;
    text-align: center; color: var(--brand-blue);
  }
  .brand-name { font-weight: 600; font-size: 22px; line-height: 1; letter-spacing: .5px; }
  .brand-sub { font-size: 6.5px; letter-spacing: 2.4px; color: var(--muted); margin-top: 3px; }
  .headline {
    position: absolute; left: 176px; top: 26px; width: 385px;
    line-height: .95; color: var(--white); white-space: nowrap;
  }
  .headline .accent { display: block; color: var(--brand-blue); font-weight: 800; font-size: 50px; letter-spacing: -.5px; }
  .headline .second { display: block; font-size: 46px; letter-spacing: -.6px; }
  .headline .lead { font-weight: 400; }
  .headline .strong { font-weight: 800; }
  .photo {
    position: absolute; top: 35px; width: 122px; height: 123px;
    border: 2px solid var(--white);
  }
  .photo-crew { left: 570px; background: linear-gradient(160deg,#6f8a5a 0%,#8a6f4f 55%,#2a2a2a 100%); }
  .photo-garage { left: 701px; background: linear-gradient(180deg,#8fa36e 0%,#6a5a52 35%,#8b6a58 50%,#e4e2dc 75%,#f1f0ec 100%); }
  .photo-walkway { left: 831px; background: linear-gradient(180deg,#7b5a44 0%,#5a463a 35%,#a45b36 65%,#b86a40 100%); }
  .web-band {
    position: absolute; left: 0; top: 148px; width: 545px; height: 53px;
    background: var(--brand-blue);
    clip-path: polygon(0 0, 100% 0, 96% 100%, 0 100%);
    display: flex; align-items: center; padding-left: 27px; gap: 10px;
    color: var(--white); font-weight: 700; font-size: 24px; white-space: nowrap;
  }
  .social {
    position: absolute; left: 548px; top: 158px; width: 420px;
    color: var(--white); font-size: 15.5px; white-space: nowrap;
    display: flex; align-items: center; gap: 5px;
  }
  .social .follow { color: var(--brand-blue); font-weight: 700; }
  .social .nets { font-weight: 600; font-size: 10px; color: var(--brand-blue); }
  .contact-bar {
    position: absolute; left: 0; top: 201px; width: 980px; height: 85px;
    background: var(--white);
  }
  .phone {
    position: absolute; left: 25px; top: 14px;
    display: flex; align-items: center; gap: 8px;
    font-weight: 800; font-size: 54px; line-height: 1; color: var(--ink); letter-spacing: -1px;
    white-space: nowrap;
  }
  .service-tag {
    position: absolute; left: 499px; top: 21px; width: 44px; height: 43px;
    background: var(--brand-blue); border-radius: 3px;
    color: var(--ink); font-weight: 600; font-size: 9px; line-height: 1.05;
    display: flex; align-items: center; justify-content: center; text-align: center;
  }
  .areas {
    position: absolute; left: 551px; top: 14px;
    display: grid; grid-template-columns: 142px 170px; row-gap: 2px;
    list-style: none; font-size: 20px; font-weight: 500; color: var(--ink); line-height: 1.2;
  }
  .areas li { display: flex; align-items: center; gap: 3px; white-space: nowrap; }
  .rating {
    position: absolute; left: 862px; top: 17px; width: 95px; text-align: center; line-height: 1;
  }
  .rating .small { font-size: 8px; font-weight: 500; color: var(--ink); }
  .rating .name { font-size: 26px; font-weight: 600; color: var(--brand-blue); margin: 1px 0; }
</style>
</head>
<body>
  <section class="billboard" aria-label="Marlowe's Construction billboard">
    <div class="brand">
      <div class="brand-name">MARLOWE’S</div>
      <div class="brand-sub">CONSTRUCTION L.L.C</div>
    </div>

    <h1 class="headline">
      <span class="accent">Concrete Built</span>
      <span class="second"><span class="lead">For </span><span class="strong">Generations</span></span>
    </h1>

    <div class="photo photo-crew" role="img" aria-label="Crew member placing a concrete form board on site"></div>
    <div class="photo photo-garage" role="img" aria-label="New concrete driveway in front of a garage"></div>
    <div class="photo photo-walkway" role="img" aria-label="Stamped terracotta concrete walkway leading to a house"></div>

    <div class="web-band">
      <svg width="32" height="32" viewBox="0 0 34 34" aria-hidden="true">
        <g fill="none" stroke="#fff" stroke-width="2.4">
          <circle cx="17" cy="17" r="14.5"/>
          <ellipse cx="17" cy="17" rx="6.5" ry="14.5"/>
          <line x1="2.5" y1="17" x2="31.5" y2="17"/>
          <line x1="17" y1="2.5" x2="17" y2="31.5"/>
          <path d="M5 9.5h24M5 24.5h24"/>
        </g>
      </svg>
      <span class="website">MarlowesConstruction.example</span>
    </div>

    <p class="social">
      <span class="follow">follow us on</span>
      <span class="nets">Chatterly · Pixtoria</span>
      <span class="handle">@marlowesconstruction</span>
    </p>

    <div class="contact-bar">
      <div class="phone">
        <svg width="43" height="43" viewBox="0 0 43 43" aria-hidden="true">
          <circle cx="21.5" cy="21.5" r="21.5" fill="#1a8fe3"/>
          <path d="M15 11c1-.6 2-.4 2.6.5l2.2 3.6c.5.9.3 1.8-.4 2.4l-1.5 1.2c1.1 2.5 3 4.5 5.4 5.7l1.3-1.4c.7-.7 1.6-.8 2.4-.3l3.5 2.3c.9.6 1.1 1.7.5 2.6l-1.4 2c-.8 1.1-2.2 1.6-3.5 1.2C19.6 29 14 23.3 12.3 16.3c-.3-1.3.2-2.6 1.3-3.4z" fill="#fff"/>
          <path d="M24 12.5a7 7 0 0 1 6.5 6.5M24 9a10.5 10.5 0 0 1 10 10" fill="none" stroke="#fff" stroke-width="1.6" stroke-linecap="round"/>
        </svg>
        <span class="number">555-214-7630</span>
      </div>

      <div class="service-tag">Service<br>Area</div>

      <ul class="areas">
        <li><svg width="9" height="13" viewBox="0 0 9 13" aria-hidden="true"><path d="M4.5 0A4.5 4.5 0 0 0 0 4.5C0 8 4.5 13 4.5 13S9 8 9 4.5A4.5 4.5 0 0 0 4.5 0zm0 6.3a1.8 1.8 0 1 1 0-3.6 1.8 1.8 0 0 1 0 3.6z" fill="#1a8fe3"/></svg>Kalamazoo</li>
        <li><svg width="9" height="13" viewBox="0 0 9 13" aria-hidden="true"><path d="M4.5 0A4.5 4.5 0 0 0 0 4.5C0 8 4.5 13 4.5 13S9 8 9 4.5A4.5 4.5 0 0 0 4.5 0zm0 6.3a1.8 1.8 0 1 1 0-3.6 1.8 1.8 0 0 1 0 3.6z" fill="#1a8fe3"/></svg>Battle Creek</li>
        <li><svg width="9" height="13" viewBox="0 0 9 13" aria-hidden="true"><path d="M4.5 0A4.5 4.5 0 0 0 0 4.5C0 8 4.5 13 4.5 13S9 8 9 4.5A4.5 4.5 0 0 0 4.5 0zm0 6.3a1.8 1.8 0 1 1 0-3.6 1.8 1.8 0 0 1 0 3.6z" fill="#1a8fe3"/></svg>Coldwater</li>
        <li><svg width="9" height="13" viewBox="0 0 9 13" aria-hidden="true"><path d="M4.5 0A4.5 4.5 0 0 0 0 4.5C0 8 4.5 13 4.5 13S9 8 9 4.5A4.5 4.5 0 0 0 4.5 0zm0 6.3a1.8 1.8 0 1 1 0-3.6 1.8 1.8 0 0 1 0 3.6z" fill="#1a8fe3"/></svg>Grand Rapids</li>
      </ul>

      <div class="rating">
        <div class="small">5 Stars</div>
        <div class="name">Zorvix</div>
        <div class="small">Rating</div>
      </div>
    </div>
  </section>
</body>
</html>
```